Haus 726 AG (real estate company)

We need a letter design including a logo for our newly founded Haus 726 AG. Haus 726 AG is a real estate company that buys and manages real estate and energy production systems such as photovoltaic systems. The number 418 in the name of the AG comes from the fact that the insurance number of the first property to be purchased has this number.
Target Market(s)
tenants of business premises
Industry/Entity Type
Immobilien
- Arial

```html
<!DOCTYPE html>
<html lang="en">
<head>
<meta charset="utf-8">
<title>Haus 726 AG – Letterhead</title>
<link rel="stylesheet" href="https://fonts.googleapis.com/css2?family=Open+Sans:wght@400;600&family=Lato:wght@400&family=Montserrat:wght@500&display=swap">
<style>
  :root {
    --backdrop: #dcdfe7;
    --paper: #ffffff;
    --brand-blue: #4e67b0;
    --brand-green: #8cc63f;
    --text: #555555;
    --watermark: #e8e8e8;
    --signature-ink: #c9ccd3;
  }
  * { margin: 0; padding: 0; box-sizing: border-box; }
  html, body { width: 1062px; height: 1200px; overflow: hidden; background: var(--backdrop); }
  .letter {
    position: absolute; left: 234px; top: 260px;
    width: 595px; height: 767px;
    background: var(--paper); overflow: hidden;
    font-family: "Open Sans", Arial, sans-serif; color: var(--text);
  }
  .brand { position: absolute; right: 54px; top: 25px; text-align: center; width: 126px; }
  .brand-dot { width: 84px; height: 84px; border-radius: 50%; background: var(--brand-green); margin: 0 auto 10px; }
  .brand-name { font-family: "Montserrat", Arial, sans-serif; font-weight: 500; font-size: 19px; color: var(--brand-blue); white-space: nowrap; }
  .watermark { position: absolute; left: 198px; top: 283px; width: 200px; height: 200px; border-radius: 50%; background: var(--watermark); }
  .block { position: absolute; left: 56px; width: 481px; font-size: 9.6px; }
  .date { top: 150px; }
  .recipient { top: 173px; line-height: 11.6px; }
  .salutation { top: 240px; }
  .body { top: 273px; line-height: 17.2px; text-align: justify; hyphens: manual; }
  .body p + p { margin-top: 17.2px; }
  .closing { top: 533px; }
  .signature { position: absolute; left: 56px; top: 558px; width: 137px; height: 18px; background: var(--signature-ink); border-radius: 2px; opacity: .5; }
  .signer-name { position: absolute; left: 56px; top: 581px; font-size: 11.8px; font-weight: 600; }
  .signer-role { top: 602px; }
  .footer-band { position: absolute; left: 0; right: 0; top: 702px; height: 65px; background: var(--brand-blue); }
  .footer-mark { position: absolute; left: -5px; top: 635px; width: 136px; height: 136px; border-radius: 50%; background: var(--paper); }
  .footer-mark::after { content: ""; position: absolute; left: 6px; top: 6px; width: 124px; height: 124px; border-radius: 50%; border: 3px solid var(--brand-blue); background: var(--paper); }
  .contact { position: absolute; left: 146px; color: #fff; font-family: "Lato", Arial, sans-serif; font-size: 11.2px; display: flex; align-items: center; gap: 7px; white-space: nowrap; }
  .contact.line-1 { top: 714px; }
  .contact.line-2 { top: 738px; }
  .contact svg { width: 11px; height: 11px; fill: #fff; flex: none; }
  .contact .item { display: flex; align-items: center; gap: 8px; margin-right: 6px; }
</style>
</head>
<body>
<main class="letter">
  <div class="watermark" aria-hidden="true"></div>

  <header class="brand">
    <div class="brand-dot" aria-hidden="true"></div>
    <div class="brand-name">Haus 726 AG</div>
  </header>

  <p class="block date">Issuing Date: May 5, 2018</p>
  <address class="block recipient" style="font-style:normal">
    Name Of Employee Mr. XYZABC<br>
    Address of Employee<br>
    Address Line 2 etc..
  </address>
  <p class="block salutation">Dear Mr.XYZABC</p>

  <div class="block body">
    <p>Lorem Ipsum has been the industry's standard dummy text ever since the 1500s, when an unknown printer took a galley of type and scrambled it to make a type specimen book. It has survived not only five centuries, but also the leap into electronic typesetting, remaining essentially unchanged. It was popularised in the 1960s with the release of Letraset sheets containing Lorem Ipsum passages, and more recently with desktop pub&shy;lishing software like Aldus PageMaker including versions of Lorem Ipsum.</p>
    <p>Lorem Ipsum is simply dummy text of the printing and typesetting industry. Lorem Ipsum has been the indus&shy;try's standard dummy text ever since the 1500s, when an unknown printer took a galley of type and scram&shy;bled it to make a type specimen book.</p>
    <p>It has survived not only five centuries, but also the leap into electronic typesetting, remaining essentially un&shy;changed. It was popularised in the 1960s with the release of Letraset sheets containing Lorem IpsumIpsum passages.</p>
  </div>

  <p class="block closing">Yours Sincerely</p>
  <div class="signature" role="img" aria-label="Handwritten signature of Martin Keller"></div>
  <p class="signer-name">Martin Keller</p>
  <p class="block signer-role">Managing Director</p>

  <div class="footer-band"></div>
  <div class="footer-mark" aria-hidden="true"></div>

  <div class="contact line-1">
    <span class="item">
      <svg viewBox="0 0 24 24"><path d="M2 9c0-3 4-5 10-5s10 2 10 5v2h-5V8.5c-1.5-.6-3-.8-5-.8s-3.5.2-5 .8V11H2zM6 12l2-3h8l2 3v7H6zm6 1.5a2.5 2.5 0 1 0 0 5 2.5 2.5 0 0 0 0-5z"/></svg>
      044-555 018 204
    </span>
    <span class="item">
      <svg viewBox="0 0 24 24"><path d="M2 5h20v14H2zm2 2v.5l8 6 8-6V7zm0 3v7h16v-7l-8 6z"/></svg>
      info@haus726ag.com
    </span>
    <span class="item">
      <svg viewBox="0 0 24 24"><path d="M12 2a10 10 0 1 0 0 20 10 10 0 0 0 0-20zm-1 3c-1 1-3 2-3 4s2 2 3 3-1 3 0 5l1 2c-4 0-7-3-7-7 0-3 2-6 6-7zm4 2c1 1 3 3 3 6l-2-1-2 1-1-2 2-2z"/></svg>
      www.haus726ag.com
    </span>
  </div>
  <div class="contact line-2">
    <span class="item">
      <svg viewBox="0 0 24 24"><path d="M12 1a8 8 0 0 0-8 8c0 6 8 14 8 14s8-8 8-14a8 8 0 0 0-8-8zm0 5a3 3 0 1 1 0 6 3 3 0 0 1 0-6z"/></svg>
      17, Lindenweg Zürich, Switzerland, 8004
    </span>
  </div>
</main>
</body>
</html>
```